card design for engineering consultancy

engineering drafting and project management company the provides drafting services for.
Electrical, Hydraulic, Mechanical, and Civil services
The company is called Q7R Services and logo is as attached
Information on card should be.
1. Logo
2.website : Q7RServices.example
3. email : info@Q7RServices.example
4. Phone: (+61) 400512836
5. Motto: Design - Document - Develop - Deliver

this card should be basically used for business identification only

Target Market(s)

electricians plumbers air conditioning installers and civil contractors

Industry/Entity Type

engineering, drafting, electrical, plumbing, airconditioning, civil

Contact Information for Business Card

1. Logo 2.website : Q7RServices.example 3. email : info@Q7RServices.example 4. Phone: (+61) 400512836 5. Motto: Design - Document - Develop - Deliver

Font styles to use
Serif

Requirements
Must have
• logo
Nice to have
• something inovative and different that makes it stand out from being just another business card

```html
<!DOCTYPE html>
<html lang="en">
<head>
<meta charset="utf-8">
<title>Q7R Services – Business Card</title>
<link rel="stylesheet" href="https://fonts.googleapis.com/css2?family=Arimo:wght@400;700&display=swap">
<style>
  :root {
    --backdrop: #e4e4e2;
    --card-white: #ffffff;
    --brand-red: #cf1a25;
    --brand-red-dark: #a50f19;
    --brand-red-light: #e0424a;
    --charcoal: #4a4747;
    --ink: #3d3d3d;
    --rule: #5a5a5a;
  }
  * { margin: 0; padding: 0; box-sizing: border-box; }
  html, body {
    width: 1200px; height: 801px; overflow: hidden;
    background: var(--backdrop);
    font-family: "Arimo", Arial, sans-serif;
  }
  .stage {
    position: relative; width: 1200px; height: 801px;
    display: flex; align-items: center; justify-content: center; gap: 40px;
  }
  .card {
    position: relative; width: 540px; height: 309px;
    box-shadow: 0 6px 18px rgba(0,0,0,0.18);
    overflow: hidden;
  }

  /* Front side */
  .card--front { background: var(--card-white); }
  .brand-block {
    position: absolute; top: 70px; left: 150px; width: 300px;
    display: flex; align-items: center; gap: 14px;
  }
  .brand-square { width: 40px; height: 40px; background: var(--charcoal); flex: none; }
  .brand-name {
    font-weight: 700; font-size: 34px; letter-spacing: 2px;
    color: var(--charcoal); text-transform: uppercase; white-space: nowrap;
  }
  .divider {
    position: absolute; left: 96px; right: 0; top: 197px;
    height: 1px; background: var(--rule);
  }
  .person { position: absolute; left: 96px; top: 150px; }
  .person-name {
    font-weight: 700; font-size: 19px; color: var(--brand-red);
    text-transform: uppercase; letter-spacing: 0.3px; line-height: 1;
  }
  .person-role { font-size: 14px; color: var(--ink); margin-top: 5px; }
  .contacts { position: absolute; left: 96px; top: 210px; list-style: none; }
  .contacts li {
    display: flex; align-items: center; gap: 10px;
    font-size: 15px; color: var(--ink); line-height: 24px;
  }
  .contacts svg { width: 13px; height: 13px; fill: var(--brand-red); flex: none; }
  .website {
    position: absolute; right: 28px; top: 208px;
    font-size: 14px; color: var(--ink);
  }

  /* Back side */
  .card--back {
    background: radial-gradient(ellipse at 35% 35%, var(--brand-red-light) 0%, var(--brand-red) 45%, var(--brand-red-dark) 100%);
  }
  .back-pattern { position: absolute; inset: 0; }
  .back-lockup {
    position: absolute; left: 50px; bottom: 44px; right: 40px;
    display: flex; align-items: flex-end; justify-content: space-between;
  }
  .back-name {
    font-weight: 700; font-size: 30px; letter-spacing: 3px;
    color: var(--card-white); text-transform: uppercase; line-height: 1;
  }
  .motto {
    font-weight: 700; font-size: 12.5px; color: var(--card-white);
    text-transform: uppercase; margin-top: 8px; letter-spacing: 0.3px;
  }
  .back-square { width: 70px; height: 44px; background: var(--card-white); border-radius: 8px; }
</style>
</head>
<body>
<main class="stage">
  <section class="card card--front" aria-label="Business card front">
    <div class="brand-block">
      <span class="brand-square"></span>
      <span class="brand-name">Q7R Services</span>
    </div>
    <div class="person">
      <p class="person-name">Daniel Harper</p>
      <p class="person-role">Manager</p>
    </div>
    <div class="divider"></div>
    <ul class="contacts">
      <li>
        <svg viewBox="0 0 24 24" aria-hidden="true"><path d="M6.6 10.8a15 15 0 0 0 6.6 6.6l2.2-2.2a1 1 0 0 1 1-.25 11.4 11.4 0 0 0 3.6.57 1 1 0 0 1 1 1V20a1 1 0 0 1-1 1A17 17 0 0 1 3 4a1 1 0 0 1 1-1h3.5a1 1 0 0 1 1 1c0 1.25.2 2.45.57 3.57a1 1 0 0 1-.25 1z"/></svg>
        (+61) 400512836
      </li>
      <li>
        <svg viewBox="0 0 24 24" aria-hidden="true"><path d="M2 5h20v14H2z M2 5l10 8 10-8" /></svg>
        info@Q7RServices.example
      </li>
    </ul>
    <p class="website">www.Q7RServices.example</p>
  </section>

  <section class="card card--back" aria-label="Business card back">
    <div class="back-pattern" role="img" aria-label="Embossed repeating brand pattern across red background"></div>
    <div class="back-lockup">
      <div>
        <p class="back-name">Q7R Services</p>
        <p class="motto">• Design • Document • Develop • Deliver</p>
      </div>
      <span class="back-square"></span>
    </div>
  </section>
</main>
</body>
</html>
```